Established food business needs a new name card design

Refer to attached current name card. Would like a new professional look design with only the company name and logo without any pictures. Would like green and yellow to be included.
To include:
My name "IBRAHIM SUKRI" and hand phone number "87260413".
To delete "
"Along Brackendale Ave 8" and
"www.nur-tiwas.com.sg"
To change email to:
"tkr27@velmorix.com.sg"

```html
<!DOCTYPE html>
<html lang="en">
<head>
<meta charset="utf-8">
<title>Nur-Tiwas Eating Corner – Name Card</title>
<link rel="stylesheet" href="https://fonts.googleapis.com/css2?family=Montserrat:wght@700&family=Roboto:wght@300&display=swap">
<style>
  :root {
    --green: #0d4a33;
    --yellow: #f2c811;
    --white: #ffffff;
    --backdrop: #e8e9eb;
  }
  * { margin: 0; padding: 0; box-sizing: border-box; }
  html, body { width: 1200px; height: 900px; overflow: hidden; }
  body { background: var(--backdrop); position: relative; font-family: "Montserrat", sans-serif; }

  .card {
    position: absolute;
    width: 620px;
    height: 354px;
    overflow: hidden;
    box-shadow: 0 6px 18px rgba(0,0,0,0.12);
  }
  .card-front { left: 90px; top: 70px; background: var(--green); }
  .card-back  { left: 490px; top: 476px; }

  .brand {
    position: absolute;
    display: flex;
    align-items: center;
    gap: 14px;
    white-space: nowrap;
    color: var(--yellow);
    font-family: "Montserrat", sans-serif;
    font-weight: 700;
    letter-spacing: 1px;
  }
  .brand-mark {
    border-radius: 50%;
    background: var(--yellow);
    flex: none;
  }
  .card-front .brand { left: 50%; top: 50%; transform: translate(-50%, -50%); font-size: 44px; }
  .card-front .brand-mark { width: 56px; height: 56px; }

  .card-back .back-art { position: absolute; inset: 0; }
  .card-back .brand { left: 44px; top: 96px; font-size: 34px; }
  .card-back .brand-mark { width: 44px; height: 44px; }

  .contact-list {
    position: absolute;
    right: 28px;
    top: 176px;
    list-style: none;
    font-family: "Roboto", sans-serif;
    font-weight: 300;
    font-size: 14px;
    color: var(--white);
    text-align: right;
  }
  .contact-item { display: flex; align-items: center; justify-content: flex-end; gap: 10px; height: 26px; white-space: nowrap; }
  .contact-icon { width: 16px; height: 16px; flex: none; }

  .holder-name {
    position: absolute;
    left: 22px;
    bottom: 14px;
    display: flex;
    align-items: center;
    gap: 12px;
    color: var(--yellow);
    font-weight: 700;
    font-size: 24px;
    letter-spacing: 1px;
  }
  .holder-dot { width: 14px; height: 14px; border-radius: 50%; background: var(--yellow); }
</style>
</head>
<body>

  <section class="card card-front">
    <div class="brand"><span class="brand-mark"></span>NUR-TIWAS</div>
  </section>

  <section class="card card-back">
    <svg class="back-art" width="620" height="354" viewBox="0 0 620 354">
      <rect width="620" height="354" fill="var(--green)"/>
      <path d="M0 0 H556 C506 186 330 296 0 298 Z" fill="var(--white)"/>
      <path d="M530 0 H548 C498 184 326 292 40 297 C300 286 480 176 530 0 Z" fill="var(--yellow)"/>
    </svg>

    <div class="brand"><span class="brand-mark"></span>NUR-TIWAS</div>

    <ul class="contact-list">
      <li class="contact-item">87260413
        <svg class="contact-icon" viewBox="0 0 16 16"><circle cx="8" cy="8" r="8" fill="var(--yellow)"/><path d="M5.2 4.5 L6.6 4.3 L7.2 6 L6.3 6.7 C6.8 7.8 7.6 8.6 8.7 9.1 L9.4 8.2 L11.1 8.8 L10.9 10.2 C8 10.4 5 7.4 5.2 4.5 Z" fill="var(--green)"/></svg>
      </li>
      <li class="contact-item">tkr27@velmorix.com.sg
        <svg class="contact-icon" viewBox="0 0 16 16"><circle cx="8" cy="8" r="8" fill="var(--yellow)"/><rect x="4" y="5.2" width="8" height="5.6" fill="none" stroke="var(--green)" stroke-width="1.1"/><path d="M4 5.4 L8 8.4 L12 5.4" fill="none" stroke="var(--green)" stroke-width="1.1"/></svg>
      </li>
    </ul>

    <div class="holder-name"><span class="holder-dot"></span>IBRAHIM SUKRI</div>
  </section>

</body>
</html>
```